Edit of flyers - text to be eddited

I currently have three flyers already designed, but want to edit the text on them. On the front of each flyer I want to delete the text which states: "50% off lawn mowing applies to first lawn mowed on any regular service and applies to first 100 callers so call now" and replace it with "Professional Lawn and Garden Maintenance".

Also on the front and rear of each flyer I want to replace the text which states "Leo and Martin" with "Martin Hollis."

All other details can stay the same thanks. I need each of the files saved as a pdf according to the instructions attached with the bleed area set as specified for printing.

Font styles to use
Serif

Colors
acd036
fbed22

Requirements
Must have
• On the front of each flyer I want to delete the text which states: "50% off lawn mowing applies to first lawn mowed on any regular service and applies to first 100 callers so call now" and replace it with "Professional Lawn and Garden Maintenance".
• Also on the front and rear of each flyer I want to replace the text which states "Leo and Martin" with "Martin Hollis."
• All other details can stay the same thanks. I need each of the files saved as a pdf according to the instructions attached with the bleed area set as specified for printing.

```html
<!DOCTYPE html>
<html lang="en">
<head>
<meta charset="utf-8">
<title>Meadowline Lawns – Flyer Set</title>
<link href="https://fonts.googleapis.com/css2?family=Baloo+2:wght@700;800&family=Montserrat:wght@500;600;700&family=Oswald:wght@500&display=swap" rel="stylesheet">
<style>
:root{
  --lime:#acd036;
  --yellow:#fbed22;
  --green-dark:#0f6b34;
  --green-mid:#1f8a3c;
  --ink:#1c1c1c;
  --page:#8a8a8a;
  --paper:#ffffff;
  --sky:#9fd2f0;
  --grass:#8cc63f;
  --pale:#eef2dc;
}
*{box-sizing:border-box;margin:0;padding:0}
html,body{width:1200px;height:1200px;overflow:hidden}
body{background:var(--page);font-family:'Montserrat',sans-serif;color:var(--ink);position:relative}
.flyer{position:absolute;left:219px;width:762px;height:360px;background:var(--paper);overflow:hidden;box-shadow:0 4px 10px rgba(0,0,0,.3)}
.flyer--one{top:30px}.flyer--two{top:420px}.flyer--three{top:810px}
.abs{position:absolute}
.photo{position:absolute}
.headline{font-family:'Baloo 2',sans-serif;font-weight:800;color:var(--green-dark);-webkit-text-stroke:0;text-shadow:-2px -2px 0 #fff,2px -2px 0 #fff,-2px 2px 0 #fff,2px 2px 0 #fff;line-height:1}
.sub{font-weight:700;color:var(--green-mid)}
.name{font-weight:700;font-size:17px}
.detail{font-weight:600;font-size:13px}
.web{font-family:'Oswald',sans-serif;font-weight:500;letter-spacing:3px;color:var(--ink);display:flex;align-items:center;gap:8px}
.web svg{flex:none}
.brand{display:flex;align-items:center;gap:7px;background:var(--paper);padding:6px 12px;border-radius:4px;font-weight:700;font-size:15px;color:var(--green-dark)}
.brand i{display:block;width:14px;height:14px;background:var(--yellow)}
/* flyer one */
.f1-photo{left:0;top:0;width:762px;height:300px;background:linear-gradient(180deg,var(--sky) 0%,#d9efc0 45%,var(--grass) 70%,#6fb52c 100%)}
.f1-band-left{left:0;top:300px;width:460px;height:60px;background:var(--lime)}
.f1-band-right{left:460px;top:300px;width:302px;height:60px;background:var(--yellow)}
/* flyer two */
.f2-photo{left:0;top:0;width:380px;height:360px;background:linear-gradient(160deg,#f3f0dc 0%,#c8d98a 40%,#7fae2e 75%,#5e8f20 100%)}
.f2-panel{left:380px;top:0;width:382px;height:360px;background:var(--yellow)}
.f2-band{left:380px;top:318px;width:382px;height:42px;background:var(--lime)}
/* flyer three */
.f3-photo{left:370px;top:0;width:392px;height:360px;background:linear-gradient(200deg,#d9ecc8 0%,#8fbf5a 40%,#4d6a3a 70%,#2b3238 100%)}
.f3-list{left:0;top:0;width:380px;height:210px;background:var(--pale)}
.f3-contact{left:0;top:210px;width:350px;height:150px;background:var(--yellow)}
.f3-webbar{left:350px;top:322px;width:412px;height:38px;background:var(--yellow)}
.services{display:grid;grid-template-columns:200px 160px;column-gap:0;row-gap:4px;font-size:13px;font-weight:600;list-style:none}
.services li::before{content:"◆";color:var(--green-dark);font-size:10px;margin-right:5px}
</style>
</head>
<body>

<section class="flyer flyer--one">
  <div class="photo f1-photo" role="img" aria-label="Sunny countryside lawn with houses, fence and blossom branches"></div>
  <h1 class="abs headline" style="left:0;width:762px;top:12px;text-align:center;font-size:37px">Professional Lawn and Garden Maintenance</h1>
  <div class="abs brand" style="left:300px;top:170px">Meadowline Lawns<i></i></div>
  <p class="abs" style="left:0;width:762px;top:242px;text-align:center;font-weight:700;font-size:25px">Lawn &amp; Garden Maintenance</p>
  <div class="abs f1-band-left"></div>
  <div class="abs f1-band-right"></div>
  <p class="abs name" style="left:16px;top:308px">Martin Hollis</p>
  <p class="abs detail" style="left:16px;top:330px">Ph : 0400555018</p>
  <p class="abs detail" style="left:180px;top:330px">Email : hello@meadowlinelawns.com.au</p>
  <p class="abs web" style="left:472px;top:318px;font-size:14px;letter-spacing:2px">
    <svg width="12" height="12" viewBox="0 0 12 12"><circle cx="6" cy="6" r="5" fill="none" stroke="#1c1c1c" stroke-width="1.5"/></svg>www.MEADOWLINELAWNS.com.au</p>
</section>

<section class="flyer flyer--two">
  <div class="photo f2-photo" role="img" aria-label="Close-up of a lawn being mowed on a bright day"></div>
  <div class="abs brand" style="left:185px;top:282px">Meadowline Lawns<i></i></div>
  <div class="abs f2-panel"></div>
  <h1 class="abs headline" style="left:380px;width:382px;top:24px;text-align:center;font-size:50px;line-height:1.1">Professional<br>Lawn &amp; Garden<br>Maintenance</h1>
  <p class="abs sub" style="left:398px;top:198px;font-size:22px">Lawn &amp; Garden Maintenance</p>
  <p class="abs name" style="left:398px;top:232px">Martin Hollis</p>
  <p class="abs detail" style="left:398px;top:258px">Ph : 0400555018</p>
  <p class="abs detail" style="left:398px;top:282px">Email : hello@meadowlinelawns.com.au</p>
  <div class="abs f2-band"></div>
  <p class="abs web" style="left:392px;top:326px;font-size:17px;letter-spacing:2px">
    <svg width="18" height="18" viewBox="0 0 18 18"><circle cx="9" cy="9" r="8" fill="none" stroke="#1c1c1c" stroke-width="2"/><path d="M1 9h16M9 1v16" stroke="#1c1c1c" stroke-width="1.5"/></svg>www.MEADOWLINELAWNS.com.au</p>
</section>

<section class="flyer flyer--three">
  <div class="photo f3-photo" role="img" aria-label="Low view of a lawn mower on green grass"></div>
  <div class="abs f3-list"></div>
  <p class="abs sub" style="left:16px;top:8px;font-size:18px;line-height:1.3;color:var(--green-dark)">At Meadowline Lawns we specialise in<br>the following services</p>
  <ul class="abs services" style="left:12px;top:58px">
    <li>Lawn mowing</li><li>Edging</li>
    <li>Blowing</li><li>Hedging</li>
    <li>Pruning</li><li>Tree Loping</li>
    <li>Weeding</li><li>Poisoning</li>
    <li>Mulching</li><li>Fertilising</li>
    <li>Rubbish removal</li><li>Planting</li>
    <li>Lawn care and advice</li><li>Turf</li>
  </ul>
  <div class="abs brand" style="left:395px;top:50px">Meadowline Lawns<i></i></div>
  <div class="abs f3-contact"></div>
  <p class="abs sub" style="left:36px;top:216px;font-size:20px">Lawn &amp; Garden Maintenance</p>
  <p class="abs detail" style="left:36px;top:246px;line-height:1.3">And any other garden maintenance job,<br>No job too big or too small.</p>
  <p class="abs name" style="left:36px;top:284px">Martin Hollis</p>
  <p class="abs detail" style="left:36px;top:310px">Ph : 0400555018</p>
  <p class="abs detail" style="left:36px;top:332px">Email : hello@meadowlinelawns.com.au</p>
  <div class="abs f3-webbar"></div>
  <p class="abs web" style="left:382px;top:328px;font-size:17px;letter-spacing:2.5px">
    <svg width="18" height="18" viewBox="0 0 18 18"><circle cx="9" cy="9" r="8" fill="none" stroke="#1c1c1c" stroke-width="2"/><path d="M1 9h16M9 1v16" stroke="#1c1c1c" stroke-width="1.5"/></svg>www.meadowlinelawns.com.au</p>
</section>

</body>
</html>
```